Hard-File Archival Services Billboard (Digitization Service) for Attorneys/Law Firms

I need a billboard design for my company "Keltor Legal Aides" that advertises our primary service: Digitization of closed client files, for law firms and attorneys. Our system works as follows: 1) We get a call about a firm that wants to digitize their archived (closed) client files (which usually find their way to file cabinets or bankers boxes), 2) We go and pick those up from the law firm, 3) We bring them to our digitization facility, scan them in, and convert them into searchable PDF/A files, and 4) We upload them on the cloud, give the client a URL to visit their files whenever they want, and we delete them when requested by the client (usually for the retention duration for Missouri's rules of professional conduct, which is 6 years). It would be really cool to see "Keltor Legal Aides" and the logo clearly on the billboard, some simple sentence relating to "Missouri's best digitizing and cloud storage service for closed client files for attorneys" (or something shorter, you get the point), with maybe a linear set of photos and arrows (as follows 1. A photo of a file cabinet opened with files hanging out of it, 2. an arrow pointing to a person scanning in documents in a big scanner (maybe with a Keltor Legal Aidess logo on it?), 3. An arrow pointing to a "secure" appearing cloud (representing cloud storage), and 4. the client sitting at a computer with an arrow pointing back to the cloud (showing the client is accessing the cloud files through the computer). Our website is www.keltorlegalaides.example if you want to glean any additional information from there. Thanks! Oh yes, I should also say the billboard dimensions (in the event you need this for photo aspect ratio) will be as follows: 14 feet tall by 48 feet wide.
Target Market(s)
Attorneys in Springfield, Missouri
Industry/Entity Type
Legal
Look and feel
Each slider illustrates characteristics of the customer's brand and the style your logo design should communicate.

```html
<!DOCTYPE html>
<html lang="en">
<head>
<meta charset="utf-8">
<title>Keltor Legal Aides — Digitize &amp; Archive Billboard</title>
<link rel="stylesheet" href="https://fonts.googleapis.com/css2?family=Anton&family=Oswald:wght@600&display=swap">
<style>
  :root {
    --page-bg: #dfe3e8;
    --board-dark: #1c1c1c;
    --board-mid: #2b2b2b;
    --brand-orange: #f0971c;
    --brand-orange-light: #f7b23a;
    --brand-orange-deep: #c8690d;
    --text-white: #ffffff;
    --text-silver: #cfcfcf;
    --tag-grey: #e4e4e4;
    --ink: #161616;
  }
  html, body {
    margin: 0;
    padding: 0;
    width: 1200px;
    height: 900px;
    overflow: hidden;
    background: var(--page-bg);
  }
  .billboard {
    position: absolute;
    left: 40px;
    top: 287px;
    width: 1120px;
    height: 325px;
  }
  .billboard svg { display: block; width: 100%; height: 100%; }
  .headline { font-family: "Anton", sans-serif; }
  .subhead { font-family: "Anton", sans-serif; }
  .band-text { font-family: "Oswald", sans-serif; font-weight: 600; }
  .tag-text { font-family: "Anton", sans-serif; }
  .brand-name { font-family: "Anton", sans-serif; }
</style>
</head>
<body>
  <div class="billboard">
    <svg viewBox="0 0 1120 325" xmlns="http://www.w3.org/2000/svg">
      <defs>
        <radialGradient id="boardShade" cx="45%" cy="40%" r="75%">
          <stop offset="0" stop-color="var(--board-mid)"/>
          <stop offset="1" stop-color="var(--board-dark)"/>
        </radialGradient>
        <linearGradient id="headlineFill" x1="0" y1="0" x2="0" y2="1">
          <stop offset="0" stop-color="var(--brand-orange-light)"/>
          <stop offset="0.55" stop-color="var(--brand-orange)"/>
          <stop offset="1" stop-color="var(--brand-orange-deep)"/>
        </linearGradient>
        <linearGradient id="subheadFill" x1="0" y1="0" x2="0" y2="1">
          <stop offset="0" stop-color="var(--text-white)"/>
          <stop offset="1" stop-color="var(--text-silver)"/>
        </linearGradient>
        <linearGradient id="bandFill" x1="0" y1="0" x2="1" y2="0">
          <stop offset="0" stop-color="var(--brand-orange-deep)"/>
          <stop offset="0.55" stop-color="#3a2a18"/>
          <stop offset="1" stop-color="var(--board-dark)"/>
        </linearGradient>
        <linearGradient id="panelFill" x1="0" y1="0" x2="1" y2="1">
          <stop offset="0" stop-color="var(--brand-orange-light)"/>
          <stop offset="1" stop-color="var(--brand-orange)"/>
        </linearGradient>
      </defs>

      <!-- board face -->
      <rect class="board-face" x="0" y="0" width="1120" height="325" fill="url(#boardShade)"/>

      <!-- orange brand panel -->
      <polygon class="brand-panel" points="984,0 1120,0 1120,325 801,325" fill="url(#panelFill)"/>

      <!-- info band -->
      <rect class="info-band" x="0" y="247" width="1120" height="46" fill="url(#bandFill)"/>

      <!-- audience tag -->
      <polygon class="audience-tag" points="938,36 1120,36 1120,74 920,74" fill="var(--tag-grey)"/>
      <text class="tag-text" x="950" y="66" font-size="27" fill="var(--ink)" textLength="148" lengthAdjust="spacingAndGlyphs">FOR ATTORNEYS</text>

      <!-- headline -->
      <text class="headline" x="35" y="139" font-size="118" fill="url(#headlineFill)" textLength="843" lengthAdjust="spacingAndGlyphs">DIGITIZE &amp; ARCHIVE</text>

      <!-- subhead -->
      <text class="subhead" x="35" y="217" font-size="53" fill="url(#subheadFill)" textLength="816" lengthAdjust="spacingAndGlyphs">CLOSED CLIENT FILES, ACCESSIBLE ONLINE</text>

      <!-- band text -->
      <text class="band-text" x="35" y="283" font-size="33" fill="var(--text-white)" textLength="1042" lengthAdjust="spacingAndGlyphs">KELTOR LEGAL AIDES - MISSOURI'S BEST DIGITIZING &amp; CLOUD STORAGE SERVICE | (417) 555-0148</text>

      <!-- brand mark -->
      <circle class="brand-dot" cx="966" cy="177" r="13" fill="var(--ink)"/>
      <text class="brand-name" x="988" y="172" font-size="30" fill="var(--ink)" textLength="112" lengthAdjust="spacingAndGlyphs">KELTOR</text>
      <text class="brand-name" x="988" y="204" font-size="26" fill="var(--ink)" textLength="112" lengthAdjust="spacingAndGlyphs">LEGAL AIDES</text>
    </svg>
  </div>
</body>
</html>
```